Property Investment eBook Cover

I am a long established Australian property investment adviser, analyst and consultant who is now in semi-retired mode and have re-branded to reflect a more casual and personal approach to advising my property investor clients. I am writing a 'revised edition' to a book written in partnership with my father 20 years ago and need an eBook Cover for this new edition. The eBook will be uploaded to all the regular Australian providers (Tarvo Reader, Quillet Epage, Zeni, Pagemarsh)

The 3 key elements in the book cover are:

Title: The Riches Engine of Land. The word 'Property' should be larger and more prominent. eg "The Wealth Power of" could be 1/3 the size of "Property" - with both justified left

Edition: Sydney 2021. "Sydney 2021" should be the focus and dominant imagery of the eBook cover and more prominent than the Title or Author

Author: Glen Markby, The Housing Numbers Guide. The word "Author" should not appear. "The Housing Numbers Guide" should appear underneath Glen Markby and justified to Glen Markby, therefore a smaller font.

The cover should be simple, but eye-catching. No property images, more of an abstract background, than a background with an image. Our preferred colour palette is more blues/greens. Prefer SerifFonts

Copy of book published 20 years ago attached for reference only

```html
<!DOCTYPE html>
<html lang="en">
<head>
<meta charset="utf-8">
<title>The Riches Engine of Land — Sydney 2021</title>
<link rel="stylesheet" href="https://fonts.googleapis.com/css2?family=Noto+Serif:wght@400;700;800&display=swap">
<style>
  :root {
    --page-bg: #e1eef2;
    --cover-top: #a9dcbc;
    --cover-mid: #aedb93;
    --cover-bottom: #9fd46c;
    --ink-dark: #2a2d2a;
    --ink-light: #ffffff;
  }
  * { margin: 0; padding: 0; box-sizing: border-box; }
  html, body {
    width: 1200px;
    height: 800px;
    overflow: hidden;
    background: var(--page-bg);
  }
  .stage {
    width: 1200px;
    height: 800px;
    display: flex;
    align-items: center;
    justify-content: center;
  }
  .book-cover {
    position: relative;
    width: 490px;
    height: 690px;
    background: linear-gradient(170deg, var(--cover-top) 0%, var(--cover-mid) 45%, var(--cover-bottom) 100%);
    font-family: "Noto Serif", Georgia, serif;
  }
  .edition {
    position: absolute;
    left: 52px;
    top: 190px;
    font-size: 40px;
    font-weight: 700;
    color: var(--ink-dark);
    letter-spacing: 0.2px;
  }
  .title {
    position: absolute;
    left: 50px;
    top: 318px;
    color: var(--ink-light);
  }
  .title-lead {
    display: block;
    font-size: 31px;
    font-weight: 700;
    line-height: 1.1;
  }
  .title-key {
    display: block;
    font-size: 98px;
    font-weight: 800;
    line-height: 1;
    margin-left: -4px;
  }
  .author {
    position: absolute;
    left: 305px;
    top: 488px;
    color: var(--ink-dark);
  }
  .author-name {
    display: block;
    font-size: 17px;
    font-weight: 700;
    line-height: 1.2;
  }
  .author-role {
    display: block;
    font-size: 10px;
    font-weight: 700;
    line-height: 1.4;
  }
</style>
</head>
<body>
  <main class="stage">
    <section class="book-cover">
      <p class="edition">Sydney 2021</p>
      <h1 class="title">
        <span class="title-lead">The Riches Engine of</span>
        <span class="title-key">Land</span>
      </h1>
      <p class="author">
        <span class="author-name">Glen Markby</span>
        <span class="author-role">The Housing Numbers Guide</span>
      </p>
    </section>
  </main>
</body>
</html>
```